Web Design Accounting-Tax and related business service online.

We are looking to develop a website/online application for users in the South African market to register and buy Accounting/tax and related services online. (New business registrations/Income tax returns/Payroll) etc

The Domain will be www.ledgerpoint-hub.co.za and the business will be run under Velmira Financial Services.

The domain - www.ledgerpoint-hub.co.za will be used as the "trading" name of the site, so any sections that possible make use name use domain name.

We are looking for designs for the website.

Here is the requirements as from the developer

• Home Page: Design of the home page of the website.
• Forms: We have different forms in the application. Need any one form designed. Just look and feel without functionality.
• Member Area: when a user will log in, the layout of dashboard to show them.

UPDATE (Previously HTML required) - Can be in PSD format for this Contest.

(If you prepared/capable to handle the PSD to HTML conversation you can quote seperate for this)

Websites that offer similar services (Not for design inspiration please, but idea of possible website layout etc)

http://www.bramblecount-web.co.za/
http://www.quillmark-enrolments.co.za/

See our current static website for colour schemes that I like.

www.velmira.co.za

Prefer clean, modern - uncluttered look.

Target Market(s)

Users that pefer employing tech and ease of obtaining services online to having Accountant physically close.

Industry/Entity Type

Business Service

Requirements
Must have
• Clean, Modern, uncluttered look.

Nice to have

Should not have
• Old "boring" stiff accounting designs. No clutter or too busy.

```html
<!DOCTYPE html>
<html lang="en">
<head>
<meta charset="utf-8">
<title>Ledgerpoint Hub – Velmira Financial Services</title>
<link href="https://fonts.googleapis.com/css2?family=Open+Sans:wght@400;600;700&family=PT+Sans+Narrow:wght@400;700&family=Titillium+Web:wght@700;900&display=swap" rel="stylesheet">
<style>
:root{
  --green:#1e8a1a;
  --green-dark:#136b10;
  --green-text:#1f8a1b;
  --lime:#5fc31e;
  --black:#000;
  --white:#fff;
  --ink:#222;
  --body:#555;
  --muted:#8a8a8a;
  --line:#d8d8d8;
}
*{margin:0;padding:0;box-sizing:border-box}
html,body{width:1033px;height:1200px;overflow:hidden}
body{position:relative;background:var(--green);font-family:"Open Sans",sans-serif;color:var(--body)}
.abs{position:absolute}

.topbar{left:0;top:0;width:1033px;height:24px;background:var(--black);color:var(--white);font-family:"PT Sans Narrow",sans-serif;font-size:15px}
.topbar .call{left:548px;top:2px;font-weight:700;display:flex;align-items:center;gap:4px}
.topbar .divider{left:688px;top:0;width:1px;height:24px;background:#555}
.topbar .login{left:698px;top:2px;color:#ddd}

.header{left:0;top:24px;width:1033px;height:113px;background:var(--white)}
.logo-mark{left:159px;top:32px;width:86px;height:86px;border-radius:50%;background:var(--lime)}
.logo-name{left:252px;top:56px;font-family:"Open Sans",sans-serif;font-weight:700;font-size:28px;color:#222;letter-spacing:1px}
.logo-sub{left:252px;top:90px;font-size:11px;color:#222;letter-spacing:2px;font-weight:700}
.logo-reg{left:252px;top:104px;font-size:6px;color:#555;font-weight:700}

.offer{left:651px;top:36px;width:207px;height:89px;background:linear-gradient(#5fc622,#2e9e13);border:1px solid #3a9e1a;color:var(--white);font-family:"PT Sans Narrow",sans-serif}
.offer .title{position:absolute;left:7px;top:3px;font-size:23px;font-weight:700;font-style:italic}
.offer .line1{position:absolute;left:7px;top:32px;font-size:15px;color:#1d5e0a}
.offer .line2{position:absolute;left:7px;top:50px;font-size:15px;color:#1d5e0a;display:flex;align-items:baseline;gap:4px}
.offer .price{font-family:"Open Sans",sans-serif;font-size:25px;color:var(--white)}

.nav{left:148px;top:147px;height:34px;display:flex;font-family:"Open Sans",sans-serif;font-size:13.5px}
.nav a{color:#bfeab2;text-decoration:none;padding:9px 13px 0;height:34px}
.nav a.active{background:var(--white);color:var(--ink);border-radius:10px 10px 0 0;padding:9px 15px 0}

.panel{left:148px;top:181px;width:722px;height:853px;background:var(--white)}
.banner{left:148px;top:181px;width:722px;height:191px;background:linear-gradient(180deg,#fbfbfb,#e3e6ea);border-bottom:3px solid #4a4a4a}
.banner-photo{left:620px;top:181px;width:250px;height:188px;background:linear-gradient(100deg,rgba(255,255,255,0),#b9c8d8 35%,#6f87a1 80%,#2a3c55)}
.banner h1{position:absolute;left:12px;top:34px;font-family:"Titillium Web",sans-serif;font-weight:900;font-size:30px;line-height:36px;color:#33a81c;text-shadow:0 0 2px #0b4e08,1px 1px 0 #0b4e08}
.banner h1 span{display:block}
.banner h1 .r{text-align:right}

.h2{font-family:"PT Sans Narrow",sans-serif;font-weight:700;font-size:27px;color:var(--ink)}
.p{font-size:9px;line-height:15px;color:var(--body)}
.welcome-h{left:161px;top:386px}
.welcome-p{left:163px;top:432px;width:350px}
.subhead{left:163px;top:467px;font-size:14.5px;color:var(--green-text)}
.video{left:162px;top:498px;width:345px;height:226px;background:radial-gradient(circle at 50% 45%,#3d7a35 0,#1f2d1f 30%,#111 65%);border:1px solid #333}
.controls{position:absolute;left:0;bottom:0;width:100%;height:26px;background:linear-gradient(#3a7a42,#1c3e22)}
.after-video{left:164px;top:734px;width:350px}
.click{left:164px;top:774px;font-size:11.5px;color:#333}
.click b{color:#1a6fc7;font-weight:400}

.about-h{left:547px;top:386px}
.about-p1{left:547px;top:434px;width:302px;text-align:justify}
.about-p2{left:547px;top:489px;width:302px;text-align:justify}

.links{left:548px;top:572px;width:300px;height:229px;border:1px solid #e3e3e3;border-radius:14px;background:linear-gradient(#fff,#f1f1f1)}
.links h3{position:absolute;left:12px;top:7px;font-family:"PT Sans Narrow",sans-serif;font-size:19px;color:var(--green-text);font-weight:700}
.links hr{position:absolute;left:12px;top:32px;width:274px;border:0;border-top:1px solid #bbb}
.links ul{position:absolute;left:22px;top:42px;list-style:none}
.links li{font-size:10px;color:#999;height:18.4px;display:flex;align-items:center;gap:9px}

.services-h{left:161px;top:820px;font-family:"PT Sans Narrow",sans-serif;font-weight:700;font-size:22px;color:var(--green-text)}
.services{left:160px;top:852px;width:697px;height:162px;border:2px solid #ddd;border-radius:5px;display:flex;padding:10px 0}
.svc{flex:1;padding:6px 12px 0;border-right:1px solid #e6e6e6;position:relative}
.svc:last-child{border-right:0}
.svc .icon{position:absolute;left:12px;top:8px;width:36px;height:32px;border-radius:4px}
.svc h4{margin-left:48px;font-size:9px;line-height:15px;color:#333;font-weight:700;height:44px;padding-top:2px}
.svc p{font-size:9px;line-height:15px;color:#666;text-align:justify}
.svc .more{position:absolute;right:12px;bottom:-6px;font-size:9px;color:var(--green-text)}

.footer{color:var(--white);font-family:Arial,"Open Sans",sans-serif}
.f-h{left:157px;top:1054px;font-size:12px;font-weight:700}
.f-addr{left:157px;top:1078px;font-size:10px;line-height:17.2px}
.f-phone{left:270px;top:1079px;font-size:10px;line-height:17.2px}
.stay{left:714px;top:1047px;font-size:11px;font-weight:700;display:flex;align-items:center;gap:4px}
.stay i{display:inline-block;width:11px;height:11px;border-radius:2px;background:#e9f3e6}
.stay i:first-child{margin-left:6px;background:#f2a33a}
.copy{left:156px;top:1177px;font-size:9.5px}
.flinks{left:498px;top:1178px;font-size:9px;color:#d5f0cd}
</style>
</head>
<body>

<div class="abs topbar">
  <div class="abs call">
    <svg width="12" height="16" viewBox="0 0 12 16"><path d="M3 1 L6 4 L4.5 6 C5 8.5 6.5 10.5 8 11.5 L10 10 L11.5 13 L9.5 15 C5 14 1.5 8 1.5 3 Z" fill="#5fc31e"/></svg>
    Call Us&nbsp; 071 555 0143
  </div>
  <div class="abs divider"></div>
  <div class="abs login">Register/login to Ledgerpoint Hub</div>
</div>

<div class="abs header"></div>
<div class="abs logo-mark"></div>
<div class="abs logo-name">VELMIRA</div>
<div class="abs logo-sub">Financial Services CC</div>
<div class="abs logo-reg">CK 2011/00000000</div>

<div class="abs offer">
  <div class="title">NEW OFFER</div>
  <div class="line1">REGISTER A NEW COMPANY FOR</div>
  <div class="line2">JUST <span class="price">₹700</span> ONLY</div>
</div>

<nav class="abs nav">
  <a class="active" href="#">HOME</a>
  <a href="#">ABOUT US</a>
  <a href="#">SERVICES</a>
  <a href="#">CLIENTFEEDBACK</a>
  <a href="#">FAQ'S</a>
  <a href="#">CONTACT US</a>
</nav>

<div class="abs panel"></div>
<div class="abs banner">
  <h1><span>Your</span><span>Accounting-Bookkeeping-Tax</span><span class="r">Partners</span></h1>
</div>
<div class="abs banner-photo" role="img" aria-label="Calculator, coins and a pen resting on a business newspaper"></div>

<h2 class="abs h2 welcome-h">Welcome to Ledgerpoint Hub</h2>
<p class="abs p welcome-p">Lorem ipsum dolor sit amet, consectetur adipiscing elit. Morbi iaculis pretium leo, eu faucibus urna ultricies non. Vestibulum eget augue quam, nec tristique neque.</p>
<div class="abs subhead">How easy to register a company with Ledgerpoint Hub</div>

<div class="abs video">
  <svg class="abs" style="left:145px;top:104px" width="66" height="66" viewBox="0 0 66 66">
    <circle cx="33" cy="33" r="31" fill="#4a4a4a" stroke="#ddd" stroke-width="3"/>
    <path d="M26 19 L46 33 L26 47 Z" fill="#eee"/>
  </svg>
  <div class="controls">
    <svg width="345" height="26" viewBox="0 0 345 26">
      <path d="M7 10 h4 l5 -4 v14 l-5 -4 h-4z" fill="#ddd"/>
      <rect x="25" y="12" width="38" height="3" rx="1.5" fill="#9fd29a"/>
      <circle cx="48" cy="13.5" r="3" fill="#cfe"/>
      <path d="M84 8 l9 5.5 -9 5.5z" fill="#eee"/>
      <rect x="103" y="10" width="162" height="6" rx="3" fill="#e9efe9"/>
      <rect x="103" y="10" width="36" height="6" rx="3" fill="#6fcf52"/>
      <circle cx="137" cy="13" r="4.5" fill="#4cae3a" stroke="#fff"/>
      <text x="274" y="17" font-size="8" fill="#fff" font-family="Open Sans,sans-serif">3.12 / 8.00</text>
      <rect x="335" y="9" width="8" height="8" fill="none" stroke="#ddd"/>
    </svg>
  </div>
</div>

<p class="abs p after-video">We offer a comprehensive range of business registrations services including CIPC registrations (including company registrations) and all SARS registrations.</p>
<div class="abs click"><b>Click here</b> to view our full range of registration services and prices.</div>

<h2 class="abs h2 about-h">About Us</h2>
<p class="abs p about-p1">Sed ut perspiciatis unde omnis iste natus error sit voluptatem accusantium doloremque laudantium, totam rem aperiam, eaque ipsa quae ab illo inventore veritatis et quasi architecto beatae vitae .</p>
<p class="abs p about-p2">Lorem ipsum dolor sit amet, consectetur adipiscing elit. Morbi iaculis pretium leo, eu faucibus urna ultricies non. Vestibulum eget augue quam, nec tristique neque. Curabitur semper arcu feugiat mi scelerisque id vehicula sem convallis. Phasellus at diam eget ligula pretium blandit vel et ante. Integer vestibulum congue nisl.</p>

<div class="abs links">
  <h3>Useful Link</h3>
  <hr>
  <ul>
    <li><svg width="9" height="8" viewBox="0 0 9 8"><path d="M0 2.5h5v-2.5l4 4-4 4v-2.5h-5z" fill="#7bbf2f"/></svg>What are the costs?</li>
    <li><svg width="9" height="8" viewBox="0 0 9 8"><path d="M0 2.5h5v-2.5l4 4-4 4v-2.5h-5z" fill="#7bbf2f"/></svg>Register A Company</li>
    <li><svg width="9" height="8" viewBox="0 0 9 8"><path d="M0 2.5h5v-2.5l4 4-4 4v-2.5h-5z" fill="#7bbf2f"/></svg>Amend a CC</li>
    <li><svg width="9" height="8" viewBox="0 0 9 8"><path d="M0 2.5h5v-2.5l4 4-4 4v-2.5h-5z" fill="#7bbf2f"/></svg>Frequently Asked Questions</li>
    <li><svg width="9" height="8" viewBox="0 0 9 8"><path d="M0 2.5h5v-2.5l4 4-4 4v-2.5h-5z" fill="#7bbf2f"/></svg>More about companies</li>
    <li><svg width="9" height="8" viewBox="0 0 9 8"><path d="M0 2.5h5v-2.5l4 4-4 4v-2.5h-5z" fill="#7bbf2f"/></svg>Company and Intellectual Property Commission</li>
    <li><svg width="9" height="8" viewBox="0 0 9 8"><path d="M0 2.5h5v-2.5l4 4-4 4v-2.5h-5z" fill="#7bbf2f"/></svg>South African Revenue Service (SARS)</li>
    <li><svg width="9" height="8" viewBox="0 0 9 8"><path d="M0 2.5h5v-2.5l4 4-4 4v-2.5h-5z" fill="#7bbf2f"/></svg>Try out our site</li>
    <li><svg width="9" height="8" viewBox="0 0 9 8"><path d="M0 2.5h5v-2.5l4 4-4 4v-2.5h-5z" fill="#7bbf2f"/></svg>Email us your queries</li>
    <li><svg width="9" height="8" viewBox="0 0 9 8"><path d="M0 2.5h5v-2.5l4 4-4 4v-2.5h-5z" fill="#7bbf2f"/></svg>Terms and Conditions</li>
  </ul>
</div>

<div class="abs services-h">OUR SERVICES</div>
<div class="abs services">
  <div class="svc">
    <div class="icon" role="img" aria-label="Business registration icon" style="background:linear-gradient(#c9b98a,#2b3c6e)"></div>
    <h4>BUSINESS<br>REGISTRATION SERVICES</h4>
    <p>Sed ut perspiciatis unde omnis iste natus error sit voluptatem accusantium doloremque laudantium, totam rem aperiam, eaque ipsa quae ab illo inve.</p>
    <span class="more">more</span>
  </div>
  <div class="svc">
    <div class="icon" role="img" aria-label="Individual services icon" style="background:linear-gradient(90deg,#3a5bb0,#e05a2a)"></div>
    <h4>INDIVIDUAL<br>SERVICES</h4>
    <p>Sed ut perspiciatis unde omnis iste natus error sit voluptatem accusantium doloremque laudantium, totam rem aperiam, eaque ipsa quae ab illo inve.</p>
    <span class="more">more</span>
  </div>
  <div class="svc">
    <div class="icon" role="img" aria-label="Business services chart icon" style="background:linear-gradient(#9fb4d6,#2d4f8e)"></div>
    <h4>BUSINESS<br>SERVICES</h4>
    <p>Sed ut perspiciatis unde omnis iste natus error sit voluptatem accusantium doloremque laudantium, totam rem aperiam, eaque ipsa quae ab illo inve.</p>
    <span class="more">more</span>
  </div>
  <div class="svc">
    <div class="icon" role="img" aria-label="Domestic workers icon" style="background:#e01f26;border-radius:50%;width:34px;height:34px"></div>
    <h4>DOMESTIC<br>WORKERS</h4>
    <p>Sed ut perspiciatis unde omnis iste natus error sit voluptatem accusantium doloremque laudantium, totam rem aperiam, eaque ipsa quae ab illo inve.</p>
    <span class="more">more</span>
  </div>
</div>

<div class="footer">
  <div class="abs f-h">Contact Us</div>
  <div class="abs f-addr">Dara Wendell<br>Lot 9 Quarry Lane,<br>Elmsford, SA, 5170<br>PO Box 482,<br>Elmsford, SA, 5170</div>
  <div class="abs f-phone">Phone Work/Mobile: 0400123456<br>Phone: 08 8000 4417<br>Fax: 08 80004418<br>Email: dara@ledgerpoint-hub.co.za</div>
  <div class="abs stay">STAY UPDATED <i></i><i></i><i></i><i></i></div>
  <div class="abs copy">© 2011-2012 Ledgerpoint Hub. All rights reserved</div>
  <div class="abs flinks">HOME | ABOUT US | &nbsp;OUR SERVICES | CLIENT FEEDBACK | FAQ | CONTACT US</div>
</div>

</body>
</html>
```